Interior designer needs a power point template design

I need a template PowerPoint design for my client presentations. The presentations I prepare for my clients usually include the furniture project, the detail of the selected furniture, and the costs. There are a lot of images I insert. What I need is to have a template that I can use for all my presentations, where from time to time I will insert the specific images and descriptions I want to insert. What will always be the same will be the cover, the colors, the font, and the design of the internal sections.
I already have my logo that I would like to insert on each page of the presentation (in small size).
In summary, I need:
- basic template design
- cover with an image chosen by Picsmeadow photo
- design an internal section/chapter
- internal page design.

I like the clolors of pink and brown <8please see image attached)
Images (will come from Picsmeadow photo)
● entrance/hall
● living room
● dining room
● Bathroom
● Closet
● Kids room
● Master bedroom
● Master bathroom
● Kitchen
● Office
● Laundry
● Balcony or Terrace

Target Market(s)

Customers (both residential and commercial projects)

Industry/Entity Type

interior design

Font styles to use
Other font styles liked:
• I like courier new

Requirements
Must have
• beautiful design
Should not have
• animations

```html
<!DOCTYPE html>
<html lang="en">
<head>
<meta charset="utf-8">
<title>Casa Lumen – Presentation Template</title>
<link rel="stylesheet" href="https://fonts.googleapis.com/css2?family=Crimson+Text:wght@400;600&display=swap">
<style>
:root{
  --board:#3a3a3a;
  --paper:#ffffff;
  --brick:#a3301f;
  --blush:#f5b6a0;
  --cocoa:#4a2318;
  --terracotta:#d4744b;
  --salmon:#e98d7a;
  --ink:#4a2318;
  --line:#9a9a9a;
}
*{box-sizing:border-box;margin:0;padding:0}
html,body{width:1200px;height:848px;overflow:hidden;background:var(--board)}
.board{position:relative;width:1200px;height:848px;background:var(--board);font-family:"Crimson Text",Georgia,serif;color:var(--ink)}
.slide{position:absolute;width:378px;height:268px;background:var(--paper);overflow:hidden}
.col-1{left:15px}.col-2{left:409px}.col-3{left:805px}
.row-1{top:12px}.row-2{top:291px}.row-3{top:568px}
.abs{position:absolute}
.photo{position:absolute}
.title{position:absolute;font-size:16.5px;letter-spacing:1.2px;font-weight:400;color:var(--ink);white-space:nowrap}
.body{position:absolute;font-size:6.4px;line-height:9.6px;text-align:center;color:var(--ink)}
.body p+p{margin-top:9px}
.on-color{color:#fff}

/* brand mark */
.brand{position:absolute;display:flex;flex-direction:column;align-items:center;width:66px}
.brand-dot{width:36px;height:36px;border:1px solid var(--line);border-radius:50%}
.brand-name{margin-top:6px;font-size:10px;letter-spacing:1.5px;color:#6e6e6e;white-space:nowrap}
.brand.light .brand-dot{border-color:rgba(255,255,255,.8)}
.brand.light .brand-name{color:#fff;font-size:17px;letter-spacing:2px}
</style>
</head>
<body>
<main class="board">

  <!-- Cover -->
  <section class="slide col-1 row-1 cover">
    <div class="photo" style="left:0;top:0;width:378px;height:268px;background:linear-gradient(100deg,#eceae7 0%,#f4f2ef 40%,#d9c7b5 75%,#a4714f 100%)" role="img" aria-label="Cover photo: dining area and living room, half sketch half rendered interior"></div>
    <svg class="abs" style="left:0;top:0" width="378" height="268" viewBox="0 0 378 268"><polygon points="0,0 90,0 152,268 0,268" fill="var(--brick)"/></svg>
    <div class="brand light" style="left:14px;top:120px;width:110px">
      <div class="brand-dot" style="width:70px;height:70px"></div>
      <div class="brand-name">CASA LUMEN</div>
    </div>
  </section>

  <!-- Our project -->
  <section class="slide col-2 row-1">
    <div class="photo" style="left:7px;top:10px;width:109px;height:80px;background:linear-gradient(135deg,#e7ddd3,#cdb9a6 60%,#3d5a48)" role="img" aria-label="Photo: living corner with arched wall and green sofa"></div>
    <div class="photo" style="left:121px;top:10px;width:124px;height:80px;background:linear-gradient(160deg,#f1ede8,#c9a77f 70%,#8a6443)" role="img" aria-label="Photo: bright dining room with wooden table"></div>
    <div class="photo" style="left:250px;top:10px;width:124px;height:80px;background:linear-gradient(150deg,#5a6470,#d2c9bd 50%,#c08a3e)" role="img" aria-label="Photo: bedroom with mustard throw"></div>
    <div class="title" style="left:0;width:378px;text-align:center;top:104px">OUR PROJECT</div>
    <div class="body" style="left:50px;width:278px;top:130px">Lorem ipsum, or lipsum as it is sometimes known, is dummy text used in laying out print, graphic or web designs. The passage is attributed to an unknown</div>
    <div class="photo" style="left:71px;top:170px;width:88px;height:67px;background:linear-gradient(160deg,#f2f0ed,#e4e0dc 60%,#2d8a93)" role="img" aria-label="Photo: kids room with teal armchair"></div>
    <div class="photo" style="left:164px;top:170px;width:102px;height:67px;background:linear-gradient(150deg,#f0e6d9,#d08a3a 50%,#243650)" role="img" aria-label="Photo: kids bedroom with navy bedding"></div>
    <div class="photo" style="left:271px;top:170px;width:103px;height:67px;background:linear-gradient(170deg,#f4f4f4,#dcdcdc 55%,#5a72a8)" role="img" aria-label="Photo: white kitchen with blue island"></div>
    <div class="abs" style="left:71px;top:244px;width:307px;height:10px;background:var(--brick)"></div>
    <div class="brand" style="left:4px;top:180px"><div class="brand-dot"></div><div class="brand-name">CASA LUMEN</div></div>
  </section>

  <!-- Living room -->
  <section class="slide col-3 row-1">
    <div class="photo" style="left:0;top:0;width:234px;height:170px;background:linear-gradient(165deg,#e9e6e1,#b8ada0 55%,#6b5a48)" role="img" aria-label="Photo: living room with beige sofa and round wooden table"></div>
    <div class="abs" style="left:234px;top:0;width:144px;height:268px;background:var(--blush)"></div>
    <div class="title" style="left:114px;top:180px">LIVING ROOM</div>
    <div class="body on-color" style="left:242px;width:128px;top:70px">
      <p>Lorem ipsum, or lipsum as it is sometimes known, is dummy text used in laying out print, graphic or web designs. The passage is attributed to an unknown</p>
      <p>Lorem ipsum, or lipsum as it is sometimes known, is dummy text used in laying out print, graphic or web designs. The passage is attributed to an unknown</p>
      <p>Lorem ipsum, or lipsum as it is sometimes known, is dummy text used in laying out print, graphic or web designs.</p>
    </div>
    <div class="brand" style="left:4px;top:183px"><div class="brand-dot"></div><div class="brand-name">CASA LUMEN</div></div>
  </section>

  <!-- Dining room -->
  <section class="slide col-1 row-2">
    <div class="title" style="left:23px;top:26px">DINING ROOM</div>
    <div class="body" style="left:14px;width:130px;top:56px">
      <p>Lorem ipsum, or lipsum as it is sometimes known, is dummy text used in laying out print, graphic or web designs. The passage is attributed to an unknown</p>
      <p>Lorem ipsum, or lipsum as it is sometimes known, is dummy text used in laying out print, graphic or web designs. The passage is attributed to an unknown</p>
    </div>
    <div class="abs" style="left:154px;top:0;width:8px;height:249px;background:var(--cocoa)"></div>
    <div class="photo" style="left:167px;top:0;width:211px;height:268px;background:linear-gradient(175deg,#dcdad6,#c6c2bb 50%,#a8733f 80%,#8b5a30)" role="img" aria-label="Photo: white kitchen with pendant lamps and wooden dining table"></div>
    <div class="brand" style="left:14px;top:180px"><div class="brand-dot"></div><div class="brand-name">CASA LUMEN</div></div>
  </section>

  <!-- Kitchen -->
  <section class="slide col-2 row-2">
    <div class="photo" style="left:0;top:0;width:378px;height:166px;background:linear-gradient(180deg,#e6e8e4,#b9cbbd 45%,#f2efe9 80%,#e0dbd4)" role="img" aria-label="Photo: green kitchen counter with white tulips in a vase"></div>
    <div class="abs" style="left:82px;top:169px;width:296px;height:99px;background:var(--terracotta)"></div>
    <div class="title on-color" style="left:82px;width:296px;text-align:center;top:178px">KITCHEN</div>
    <div class="body on-color" style="left:95px;width:270px;top:203px">
      <p>Lorem ipsum, or lipsum as it is sometimes known, is dummy text used in laying out print, graphic or web designs. The passage is attributed to an unknown</p>
      <p>Lorem ipsum, or lipsum as it is sometimes known, is dummy text used in laying out print, graphic or web designs. The passage is attributed to an unknown</p>
    </div>
    <div class="brand" style="left:8px;top:180px"><div class="brand-dot"></div><div class="brand-name">CASA LUMEN</div></div>
  </section>

  <!-- Bed room -->
  <section class="slide col-3 row-2">
    <div class="abs" style="left:0;top:17px;width:99px;height:6px;background:var(--brick)"></div>
    <div class="abs" style="left:80px;top:28px;width:110px;height:214px;background:var(--brick)"></div>
    <div class="title on-color" style="left:80px;width:110px;text-align:center;top:40px">BED ROOM</div>
    <div class="body on-color" style="left:92px;width:86px;top:64px">
      <p>Lorem ipsum, or lipsum as it is sometimes known, is dummy text used in laying out print, graphic or web designs. The passage is attributed to an unknown</p>
      <p>Lorem ipsum, or lipsum as it is sometimes known, is dummy text used in laying out print, graphic or web designs. The passage is attributed to an unknown</p>
    </div>
    <div class="photo" style="left:195px;top:28px;width:183px;height:214px;background:linear-gradient(180deg,#5f6b52,#76805f 40%,#b07a63 60%,#e8e6e3 85%)" role="img" aria-label="Photo: bed with pink headboard against green wall"></div>
    <div class="abs" style="left:294px;top:247px;width:84px;height:6px;background:var(--brick)"></div>
    <div class="brand" style="left:4px;top:180px"><div class="brand-dot"></div><div class="brand-name">CASA LUMEN</div></div>
  </section>

  <!-- Kids room -->
  <section class="slide col-1 row-3">
    <div class="title" style="left:47px;top:46px">KIDS ROOM</div>
    <div class="body" style="left:26px;width:150px;top:74px">
      <p>Lorem ipsum, or lipsum as it is sometimes known, is dummy text used in laying out print, graphic or web designs. The passage is attributed to an unknown</p>
      <p>Lorem ipsum, or lipsum as it is sometimes known, is dummy text used in laying out print, graphic or web designs. The passage is attributed to an unknown</p>
    </div>
    <div class="photo" style="left:184px;top:28px;width:88px;height:88px;border-radius:50%;background:radial-gradient(circle at 40% 40%,#e8dccb,#8fa7b5 70%)" role="img" aria-label="Photo: kids room with bunk bed"></div>
    <div class="photo" style="left:278px;top:26px;width:88px;height:88px;border-radius:50%;background:radial-gradient(circle at 60% 40%,#efe3d2,#c27a3a 55%,#23324a)" role="img" aria-label="Photo: kids bed with navy blanket"></div>
    <div class="photo" style="left:184px;top:121px;width:88px;height:88px;border-radius:50%;background:radial-gradient(circle at 50% 40%,#f6eee6,#e9b79c 60%,#c9a47d)" role="img" aria-label="Photo: nursery with pink canopy"></div>
    <div class="photo" style="left:278px;top:118px;width:88px;height:88px;border-radius:50%;background:radial-gradient(circle at 50% 35%,#f3ede6,#e18a45 55%,#6c7b8e)" role="img" aria-label="Photo: playroom with grey sofa and orange cushions"></div>
    <div class="abs" style="left:70px;top:242px;width:308px;height:11px;background:var(--salmon)"></div>
    <div class="brand" style="left:8px;top:180px"><div class="brand-dot"></div><div class="brand-name">CASA LUMEN</div></div>
  </section>

  <!-- Bathroom -->
  <section class="slide col-2 row-3">
    <div class="photo" style="left:120px;top:150px;width:258px;height:118px;background:linear-gradient(180deg,rgba(235,235,235,0),#f0f0f0 40%,#e6e4e1)" role="img" aria-label="Faded photo: light bathroom with basin"></div>
    <div class="photo" style="left:0;top:14px;width:221px;height:152px;background:linear-gradient(160deg,#6e7f5a,#e8e8e8 40%,#cfcfcf 65%,#2a2a2a)" role="img" aria-label="Photo: marble bathroom with freestanding tub and glass shower"></div>
    <div class="abs" style="left:226px;top:14px;width:152px;height:46px;background:var(--cocoa)"></div>
    <div class="title on-color" style="left:226px;width:152px;text-align:center;top:25px">BATHROOM</div>
    <div class="body" style="left:234px;width:136px;top:74px">
      <p>Lorem ipsum, or lipsum as it is sometimes known, is dummy text used in laying out print, graphic or web designs. The passage is attributed to an unknown</p>
      <p>Lorem ipsum, or lipsum as it is sometimes known, is dummy text used in laying out print, graphic or web designs. The passage is attributed to an unknown</p>
    </div>
    <div class="abs" style="left:80px;top:172px;width:141px;height:12px;background:var(--cocoa)"></div>
    <div class="brand" style="left:6px;top:180px"><div class="brand-dot"></div><div class="brand-name">CASA LUMEN</div></div>
  </section>

  <!-- Laundry -->
  <section class="slide col-3 row-3">
    <div class="photo" style="left:0;top:5px;width:378px;height:160px;background:linear-gradient(180deg,#2e2e2e,#8a7a6a 45%,#c9ab86 78%,#b08a60)" role="img" aria-label="Photo: laundry room with basin on wooden counter and washing machine"></div>
    <div class="title" style="left:0;width:378px;text-align:center;top:134px">LAUNDRY</div>
    <div class="body" style="left:96px;width:270px;top:180px">
      <p>Lorem ipsum, or lipsum as it is sometimes known, is dummy text used in laying out print, graphic or web designs. The passage is attributed to an unknown</p>
      <p>Lorem ipsum, or lipsum as it is sometimes known, is dummy text used in laying out print, graphic or web designs. The passage is attributed to an unknown</p>
    </div>
    <div class="abs" style="left:102px;top:246px;width:276px;height:6px;background:var(--terracotta)"></div>
    <div class="brand" style="left:6px;top:180px"><div class="brand-dot"></div><div class="brand-name">CASA LUMEN</div></div>
  </section>

</main>
</body>
</html>
```